BRAMLEIGH real estate family office

Hello, Our business is a real estate intermediation activity on high-end goods (amounts exceeding € 10m) for corporate and private clients. You can see our logo on the site www.bramleigh-invented.fr We would like to keep that spirit with the hexagon that represents France (transactions between Monaco and Saint Tropez, Courchevel and Paris). And the "baseline" that is "real estate family office". The corporate logo should be and can be printed by embossing (relief). We must integrate the name, first name, phone, email and website. Finally, to imbibe the spirit of business, here is a detail of the activity. "Genuine consulting firm in real estate investments, BRAMLEIGH works with its customers as a specialized player in the high-end markets, we are recognized for our ultra-confidential approach and tailor-made, as well as the quality of our network. We broadcast any information on the market and we work exclusively through a strong relationship we have developed over the years. BRAMLEIGH is active on the French Riviera (from Monaco to Saint-Tropez), the Alps (Courchevel, Méribel, Megève) and Paris (essentially market premium). Always looking for opportunities for our clients, we work on two investment areas: residential luxury real estate (properties, vineyards, mansions, land, etc.) commercial real estate (empty office buildings or yield, hotel properties, land, etc.) "

Target Market(s)

High foreign end customers. corporate and private.

Industry/Entity Type

Real Estate

Contact Information for Business Card

LOGO
baseline
Laurent Dufossé
+33(0)6.41.57.09.64
ld@bramleigh-invented.fr
www.bramleigh-invented.fr

Font styles to use
Serif

Colors
cedeed
0255a3
3277b5
85abd2
85cae6
34a7d7
0792cd
cfdeed
1b1b1b

Requirements
Must have
• see description

```html
<!DOCTYPE html>
<html lang="fr">
<head>
<meta charset="utf-8">
<title>BRAMLEIGH – business cards</title>
<link href="https://fonts.googleapis.com/css2?family=Didact+Gothic&family=Roboto:wght@400;500&display=swap" rel="stylesheet">
<style>
  :root{
    --bg:#ecebe8;
    --blue:#0255a3;
    --blue-deep:#0346a8;
    --blue-light:#0a5cc8;
    --white:#ffffff;
    --paper:#f4f4f4;
    --grey:#8e8e8e;
    --grey-text:#7d7d7d;
    --ink:#1b1b1b;
  }
  html,body{margin:0;padding:0;}
  body{
    width:1200px;height:1023px;overflow:hidden;
    background:var(--bg);
    position:relative;
    font-family:"Roboto",Arial,sans-serif;
  }
  .card{
    position:absolute;
    width:540px;height:310px;
    border-radius:16px;
    overflow:hidden;
    box-shadow:0 4px 14px rgba(0,0,0,.18);
  }
  /* front */
  .card--front{left:40px;top:356px;background:linear-gradient(160deg,var(--white),var(--paper));}
  .front__panel{position:absolute;left:0;top:0;width:540px;height:310px;}
  .wordmark{
    position:absolute;
    font-family:"Didact Gothic","Century Gothic",sans-serif;
    color:var(--grey-text);
    letter-spacing:4px;
    line-height:1;
  }
  .baseline{
    position:absolute;
    font-family:"Didact Gothic","Century Gothic",sans-serif;
    color:var(--blue);
    letter-spacing:1px;
    line-height:1;
  }
  .card--front .wordmark{left:236px;top:44px;font-size:46px;}
  .card--front .baseline{left:300px;top:98px;font-size:15px;}
  .namebox{
    position:absolute;left:22px;top:150px;
    width:238px;height:58px;
    background:var(--grey);
    color:var(--white);
    padding:8px 14px;box-sizing:border-box;
  }
  .namebox__name{font-size:21px;font-weight:500;letter-spacing:.5px;line-height:1.1;}
  .namebox__role{font-size:12px;margin-top:3px;}
  .contacts{
    position:absolute;left:300px;top:214px;
    margin:0;padding:0;list-style:none;
    color:var(--white);font-size:12px;letter-spacing:1px;
  }
  .contacts li{display:flex;align-items:center;gap:10px;height:24px;}
  .contacts svg{width:12px;height:12px;flex:none;}
  /* back */
  .card--back{left:620px;top:356px;background:linear-gradient(170deg,var(--blue-light),var(--blue-deep));}
  .back__band{position:absolute;left:0;top:68px;width:540px;height:150px;background:linear-gradient(90deg,var(--paper),var(--white));}
  .card--back .wordmark{left:100px;top:98px;font-size:52px;}
  .card--back .baseline{left:110px;top:164px;font-size:16px;}
</style>
</head>
<body>

<section class="card card--front" aria-label="Front of card">
  <svg class="front__panel" viewBox="0 0 540 310" aria-hidden="true">
    <defs>
      <linearGradient id="frontBlue" x1="0" y1="0" x2="1" y2="1">
        <stop offset="0" stop-color="#0a5cc8"/>
        <stop offset="1" stop-color="#0346a8"/>
      </linearGradient>
    </defs>
    <path d="M0 118 H60 L90 100 H300 L250 150 H540 V310 H0 Z" fill="url(#frontBlue)"/>
  </svg>
  <div class="wordmark">BRAMLEIGH</div>
  <div class="baseline">real estate family office</div>

  <div class="namebox">
    <div class="namebox__name">Laurent Dufossé</div>
    <div class="namebox__role">Managing Partner</div>
  </div>

  <ul class="contacts">
    <li>
      <svg viewBox="0 0 12 12"><circle cx="6" cy="6" r="5.3" fill="none" stroke="#fff" stroke-width="1"/><path d="M4 3.2c-.6.4-.7 1.2-.2 2.2.6 1.3 1.7 2.4 2.9 2.9.9.4 1.6.3 2-.3L7.5 7l-.7.5C6 7.2 5 6.2 4.6 5.3l.5-.7z" fill="#fff"/></svg>
      <span>+33(0)6.41.57.09.64</span>
    </li>
    <li>
      <svg viewBox="0 0 12 12"><rect x="1" y="2.5" width="10" height="7" fill="none" stroke="#fff" stroke-width="1"/><path d="M1 2.5l5 4 5-4" fill="none" stroke="#fff" stroke-width="1"/></svg>
      <span>ld@bramleigh-invented.fr</span>
    </li>
    <li>
      <svg viewBox="0 0 12 12"><circle cx="6" cy="6" r="5" fill="none" stroke="#fff" stroke-width="1"/><ellipse cx="6" cy="6" rx="2.2" ry="5" fill="none" stroke="#fff" stroke-width=".8"/><path d="M1 6h10M2 3.5h8M2 8.5h8" stroke="#fff" stroke-width=".7"/></svg>
      <span>www.bramleigh-invented.fr</span>
    </li>
  </ul>
</section>

<section class="card card--back" aria-label="Back of card">
  <div class="back__band"></div>
  <div class="wordmark">BRAMLEIGH</div>
  <div class="baseline">real estate family office</div>
</section>

</body>
</html>
```